Jobinserat Vorlage medizinischer Bereich
Sehr gute Kommunikation auch mit Rückfragen damit das Projekt komplett verstanden wurde. Schnelle Umsetzung mit tollen Vorschlägen. Nur zu empfehlen!
Zielgruppe
Personalagentur im medizinischen Bereich (Krankenpfleger/Fachärzte)
Zielgruppe: Jobsuchende Krankenpflege Fachleute in Deutschland für die Schweiz!
Aufgabenstellung
jung, frisch, emotionell, verlockend
Bitte Text beachten: klinikpflegeleiterin
Wir benötigen ein Layout für ein Stelleninserat welches wir auf bei www.pflegestellenboerse.de platzieren möchten sowie auf www.medizinerkarriere.de / Das Format wird A4 sein, entweder eine oder zwei Seiten, je nachdem was für eine Stelle wir ausschreiben. Wichtig ist das Logo und der Text (siehe Projektanlage). Als Anhaltspunkt geht das Inserat (http://www.pflegestellenboerse.de/job/dipl-pflegefachfraudipl-pflegefachmann-hffh-oder-fage-fur-kurzeinsatze-10-20) in die Richtige Richtung, einfach mit unserer Farbe vom Logo oder der Academy http://www.valorintgruppe.com/academy/

```html
<!DOCTYPE html>
<html lang="de">
<head>
<meta charset="utf-8">
<title>Stelleninserat Klinikpflegeleitung</title>
<link href="https://fonts.googleapis.com/css2?family=Source+Sans+3:ital,wght@0,400;0,600;0,700;1,600;1,700&display=swap" rel="stylesheet">
<style>
  :root{
    --orange:#eea81f;
    --teal-dark:#47b3a6;
    --teal-light:#a6ddd5;
    --charcoal:#454545;
    --text:#333333;
    --grey:#6d6d6d;
    --white:#ffffff;
    --bg:#f4f4f4;
  }
  *{margin:0;padding:0;box-sizing:border-box}
  html,body{width:1200px;height:1200px;overflow:hidden;background:var(--bg)}
  body{font-family:"Source Sans 3",Arial,sans-serif;color:var(--text);position:relative}
  .sheet{position:absolute;left:241px;top:94px;width:716px;height:1010px;background:var(--white);overflow:hidden}
  .top-rule{position:absolute;left:0;top:0;width:100%;height:7px;background:var(--orange)}
  .hero{position:absolute;left:0;top:7px;width:100%;height:285px;
    background:radial-gradient(circle at 70% 55%,var(--teal-light) 0%,#7fcbc0 45%,var(--teal-dark) 100%)}
  .hero-photo{position:absolute;left:40px;top:7px;width:330px;height:285px;
    background:linear-gradient(180deg,#9c8a7a 0%,#e9e4de 55%,#d4cfc9 100%);opacity:.55}
  .hero-quote{position:absolute;right:67px;top:86px;width:420px;text-align:right;color:var(--white);
    font-style:italic;font-weight:700;font-size:16px;line-height:20px}
  .hero-quote .l2{margin-right:0}
  .hero-quote .l3{margin-right:0}
  .hero-quote cite{display:block;font-size:9.5px;line-height:14px;margin-top:2px;margin-right:48px}
  .hero-teaser{position:absolute;left:404px;top:183px;color:var(--white);font-weight:600;font-size:17px;line-height:21px}
  .tag{position:absolute;left:0;top:263px;width:248px;height:50px;background:var(--orange);
    color:var(--charcoal);font-size:37px;font-weight:600;line-height:50px;padding-left:30px}
  .title-band{position:absolute;left:0;top:320px;width:100%;height:49px;background:var(--charcoal);
    color:var(--white);font-size:27px;font-weight:600;line-height:49px;padding-left:95px;letter-spacing:.2px}
  .content{position:absolute;left:96px;top:390px;width:532px;font-size:12px;line-height:15px}
  .content h2{font-size:13.5px;font-weight:700;color:var(--text);margin:0 0 6px}
  .content ul{list-style:none;margin-bottom:12px}
  .content li{position:relative;padding-left:14px;margin-bottom:3px}
  .content li::before{content:"";position:absolute;left:0;top:4px;width:6px;height:6px;background:var(--orange)}
  .content p{margin-bottom:12px}
  .content strong{font-weight:700}
  .content .justify li{text-align:justify}
  .adviser{position:absolute;left:96px;top:875px;font-size:12px;line-height:15px}
  .adviser h3{font-size:12px;font-weight:700;margin-bottom:6px}
  .social{margin-top:12px;display:flex;align-items:center;gap:5px}
  .social .square{width:13px;height:13px;background:#3b5998}
  .brand{position:absolute;left:412px;top:900px;display:flex;align-items:center;gap:10px}
  .brand .mark{width:20px;height:20px;background:var(--orange)}
  .brand .name{font-size:23px;font-weight:400;color:var(--grey);line-height:26px}
  .brand-address{position:absolute;left:412px;top:962px;font-size:8.5px;font-weight:600;line-height:11px;color:var(--text)}
  .bottom-rule{position:absolute;left:0;bottom:0;width:100%;height:7px;background:var(--charcoal)}
</style>
</head>
<body>
  <main class="sheet">
    <div class="top-rule"></div>
    <div class="hero" role="img" aria-label="Türkiser Hintergrund mit Foto eines jungen Arztes mit Brille, roter Fliege und erhobenem Zeigefinger"></div>
    <div class="hero-photo" role="img" aria-label="Fotobereich: junger Arzt im weissen Kittel"></div>
    <blockquote class="hero-quote">
      „Wir müssen uns vor Augen halten,<br>
      <span class="l2">dass wir unsere Vergangenheit selbst gestalten</span><br>
      <span class="l3">und zwar durch das, was wir heute tun.“</span>
      <cite>– Stationsgeflüster –</cite>
    </blockquote>
    <p class="hero-teaser">Ihr neuer Job in der schönen Schweiz<br>könnte ein Anfang sein...</p>

    <div class="tag">Wir suchen</div>
    <h1 class="title-band">Klinikpflegeleiterin / Klinikpflegeleiter</h1>

    <section class="content">
      <h2>Ihre Aufgaben:</h2>
      <ul class="justify">
        <li>Sicherstellung einer wirksamen, wirtschaftlichen und zweckmässigen Pflege und Betreuung</li>
        <li>Führung und Förderung der unterstellten Mitarbeitenden inklusive Stellenplanbewirtschaftung</li>
        <li>Mitwirkung bei der strategischen Weiterentwicklung von unternehmensweiten Projekten<br>und Kliniken</li>
        <li>Gewährleistung des Ausbildungsauftrages auf der Grund- und Tertiärstufe</li>
        <li>Qualitätssicherung und Prozessoptimierung gemäss der Unternehmensstrategie</li>
      </ul>
      <h2>Anfoderungen:</h2>
      <ul>
        <li>Dipl. Pflegefachfrau/-mann HF, DN II, AKP, FH, DGKS</li>
        <li>Fundierte Führungserfahrung mit einer ausgewiesenen Managementweiterbildung auf<br>Fachhochschulniveau oder einer vergleichbaren Weiterbildung</li>
        <li>Hohe Patientenorientierung</li>
        <li>Konzeptionelle Fähigkeiten verbunden mit Innovationskraft und unternehmerischen Denken<br>und Handeln</li>
        <li>Kommunikative und teamorientierte Persönlichkeit mit betriebswirtschaftlichen und<br>organisatorischen Fähigkeiten</li>
        <li>Engagement für eine interdisziplinäre und interprofessionelle Zusammenarbeit mit einem<br>hohen Mass an Verantwortungsbereitschaft</li>
      </ul>
      <p>Suchen Sie eine verantwortungsvolle Herausforderung in einem familiären, dynamischen Umfeld<br>mit attraktiven Entwicklungsmöglichkeiten?</p>
      <p><strong>Wir garantieren Ihnen absolute Diskretion.</strong></p>
      <p>Für einen ersten vertraulichen Kontakt steht Ihnen Herr <strong>Lukas Brenner</strong> gerne zur Verfügung.<br>
        Zögern Sie nicht, wir freuen uns auf Ihre komplette online Bewerbung mit Foto per E-Mail an:<br>
        <strong>lukas.brenner@valorintgruppe.com</strong></p>
    </section>

    <section class="adviser">
      <h3>Ihr Berater:</h3>
      <p>Lukas Brenner<br>Tel. +41 44 600 27 15<br>Mail: lukas.brenner@valorintgruppe.com<br>Web: valorintgruppe.com</p>
      <div class="social">Finde uns auf <span class="square" aria-label="Socialia"></span></div>
    </section>

    <div class="brand">
      <span class="mark"></span>
      <span class="name">Valorint<br>Recruitment Group</span>
    </div>
    <p class="brand-address">Valorint – Recruitment Group Ltd.<br>Brunnmattstrasse 4 | CH-6370 Oberdorf</p>

    <div class="bottom-rule"></div>
  </main>
</body>
</html>
```